Kneadwell Bodycare

We are a Massage Therapy business based in Invercargill, New Zealand. We specialise in Sports and deep tissue massage but also provide relaxation and aromatherapy massage. We would like to see designs that use the the logo.
The final design should promote health and fitness.
Updates

Hi I am getting feedback that my business card picture is poor quality. I got this picture from plaza press under massage. So if you google this image a better quality picture should come up,. If not hope to upload a better image by tomorow, thanks.

Target Market(s)

Sports, people with pain and injuries

Industry/Entity Type

Massage

Requirements
Must have
• Logo, muscle body that is used on the business card, also a poster that matches my business card
Nice to have
• Picture of muscle man, shown on my business card
Should not have
• Not a picture of a real person

```html
<!DOCTYPE html>
<html lang="en">
<head>
<meta charset="utf-8">
<title>Kneadwell Bodycare Poster</title>
<link rel="stylesheet" href="https://fonts.googleapis.com/css2?family=Oswald:wght@400;500;600;700&display=swap">
<style>
  :root {
    --navy: #2b3576;
    --sky: #4ea3dc;
    --pale: #d9ebf7;
    --white: #ffffff;
    --figure-light: #e6e8ec;
    --figure-dark: #9aa0aa;
  }
  * { margin: 0; padding: 0; box-sizing: border-box; }
  html, body { width: 851px; height: 1200px; overflow: hidden; background: var(--white); }
  .poster {
    position: relative;
    width: 851px;
    height: 1200px;
    overflow: hidden;
    background: var(--white);
    font-family: "Oswald", "Arial Narrow", sans-serif;
    color: var(--navy);
  }
  .hero-figure {
    position: absolute;
    left: 0; top: 0;
    width: 420px; height: 330px;
    background: radial-gradient(ellipse at 40% 45%, var(--figure-light) 0%, #c8ccd3 55%, rgba(255,255,255,0) 80%);
  }
  .headline {
    position: absolute;
    right: 32px;
    text-align: right;
    text-transform: uppercase;
    line-height: 1;
  }
  .headline-top { top: 28px; font-size: 118px; font-weight: 500; color: var(--navy); letter-spacing: 1px; }
  .headline-main { top: 150px; font-size: 170px; font-weight: 500; color: var(--sky); letter-spacing: 2px; }
  .brand-band {
    position: absolute;
    left: 0; top: 335px;
    width: 851px; height: 135px;
    background: var(--navy);
    border-top: 6px solid var(--sky);
    display: flex;
    align-items: center;
    padding-left: 38px;
  }
  .brand-mark {
    width: 100px; height: 100px;
    border-radius: 50%;
    background: var(--white);
    flex: none;
  }
  .brand-name {
    margin-left: 30px;
    color: var(--white);
    font-size: 66px;
    font-weight: 400;
    letter-spacing: 0.5px;
  }
  .backdrop-ring {
    position: absolute;
    left: 420px; top: 610px;
    width: 620px; height: 620px;
    border-radius: 50%;
    border: 90px solid var(--pale);
  }
  .services {
    position: absolute;
    left: 68px; top: 512px;
    list-style: none;
    font-size: 50px;
    font-weight: 500;
    line-height: 70px;
    color: var(--navy);
  }
  .booking {
    position: absolute;
    left: 478px; top: 508px;
    line-height: 1.15;
  }
  .booking-lead { font-size: 38px; color: var(--sky); font-weight: 500; }
  .booking-phone { font-size: 38px; color: var(--navy); font-weight: 500; }
  .prices {
    position: absolute;
    left: 478px; top: 672px;
    line-height: 48px;
  }
  .prices-title { font-size: 38px; color: var(--sky); font-weight: 500; text-transform: uppercase; }
  .prices-list { list-style: none; font-size: 38px; color: var(--navy); font-weight: 500; }
  .credentials {
    position: absolute;
    left: 0; top: 942px;
    width: 851px;
    text-align: center;
    color: var(--navy);
  }
  .credentials-name { font-size: 32px; font-weight: 500; }
  .credentials-contact { margin-top: 12px; font-size: 28px; font-weight: 400; }
  .credentials-contact .divider { margin: 0 22px; }
  .social {
    margin-top: 26px;
    font-size: 30px;
    font-weight: 500;
    display: inline-flex;
    align-items: center;
    gap: 12px;
  }
  .social-dot { width: 26px; height: 26px; background: var(--navy); border-radius: 4px; }
</style>
</head>
<body>
  <div class="poster">
    <div class="hero-figure" role="img" aria-label="Anatomical illustration of a muscular upper body with shoulder and arm muscles highlighted"></div>

    <div class="headline headline-top">Are you in</div>
    <div class="headline headline-main">Pain?</div>

    <div class="backdrop-ring"></div>

    <header class="brand-band">
      <div class="brand-mark"></div>
      <div class="brand-name">Kneadwell Bodycare</div>
    </header>

    <ul class="services">
      <li>Deep Tissue</li>
      <li>Sports Massage</li>
      <li>Remedial Massage</li>
      <li>Relaxation</li>
      <li>Aromatherapy</li>
    </ul>

    <div class="booking">
      <div class="booking-lead">Book today!</div>
      <div class="booking-phone">Call 0271 486 205</div>
    </div>

    <div class="prices">
      <div class="prices-title">Prices</div>
      <ul class="prices-list">
        <li>30 minutes: $40</li>
        <li>60 minutes: $60</li>
        <li>90 minutes: $80</li>
      </ul>
    </div>

    <footer class="credentials">
      <div class="credentials-name">Mara Delaney, Bachelor of Therapeutic &amp; Sports Massage</div>
      <div class="credentials-contact">18 Kelvin Rd, Invercargill<span class="divider">|</span>www.kneadwell.co.nz</div>
      <div class="social">Like us on Friendloop <span class="social-dot"></span></div>
    </footer>
  </div>
</body>
</html>
```